Simple proffessional BC

I have a logo which I will attach below.
I would like the logo on the front of the card with these details in point form below:
Pre and Post Natal Yoga: Pregnancy Workshops: Hypnobirthing Courses
On the back of the card my details:
Marla Penrick
Facebook page- calmcradlestudiolakebay
Mobile- 0482 315 746

I like the idea of the card being simple, possibly just the above on a plain coloured (eggshell?) card, a card that is textured.
I am open to suggestion if it appeals!
Thank you and good luck!

Target Market(s)

Pregnant women, 20's-40's

Requirements
Must have
• Simple, compliment logo.
Make logo the feature.
Should not have

```html
<!DOCTYPE html>
<html lang="en">
<head>
<meta charset="utf-8">
<title>Calm Cradle – Business Card</title>
<link rel="stylesheet" href="https://fonts.googleapis.com/css2?family=Pinyon+Script&family=Raleway:wght@300&family=Share+Tech+Mono&display=swap">
<style>
  :root {
    --saffron: #eea63a;
    --maroon: #7b1c1e;
    --card-white: #f6f6f4;
    --backdrop: #d9d9d9;
    --contact-ink: #fff8ec;
  }
  * { margin: 0; padding: 0; box-sizing: border-box; }
  html, body {
    width: 1037px;
    height: 1200px;
    overflow: hidden;
    background: var(--backdrop);
  }
  .canvas {
    position: relative;
    width: 1037px;
    height: 1200px;
  }
  .card {
    position: absolute;
    left: 98px;
    width: 840px;
    height: 480px;
    background: var(--card-white);
    box-shadow: 0 6px 18px rgba(0,0,0,0.18);
    overflow: hidden;
  }
  .card--back { top: 80px; }
  .card--front { top: 640px; }

  /* Back side */
  .details-band {
    position: absolute;
    left: 0; top: 0;
    width: 100%;
    height: 310px;
    background: var(--saffron);
  }
  .holder-name {
    position: absolute;
    left: 60px;
    top: 112px;
    width: 330px;
    text-align: center;
    font-family: "Pinyon Script", cursive;
    font-size: 52px;
    color: var(--maroon);
  }
  .divider {
    position: absolute;
    left: 390px;
    top: 54px;
    width: 3px;
    height: 230px;
    background: var(--maroon);
  }
  .contact {
    position: absolute;
    left: 418px;
    display: flex;
    align-items: center;
    gap: 14px;
    color: var(--contact-ink);
    font-family: "Share Tech Mono", monospace;
  }
  .contact--social { top: 92px; font-size: 17px; letter-spacing: 2px; }
  .contact--phone { top: 150px; font-size: 36px; letter-spacing: 5px; }
  .social-dot {
    width: 20px; height: 20px;
    border-radius: 50%;
    background: #3b5ea8;
    flex: none;
  }
  .phone-icon { width: 16px; height: 26px; flex: none; }

  .brand-band {
    position: absolute;
    left: 0; top: 310px;
    width: 100%;
    height: 170px;
    display: flex;
    align-items: center;
    padding-left: 42px;
    gap: 26px;
  }
  .brand-disc {
    width: 128px; height: 128px;
    border-radius: 50%;
    background: var(--saffron);
    flex: none;
  }
  .brand-name {
    font-family: "Raleway", sans-serif;
    font-weight: 300;
    color: var(--maroon);
    font-size: 74px;
    line-height: 1;
  }

  /* Front side */
  .front-lockup {
    position: absolute;
    left: 0; top: 120px;
    width: 100%;
    display: flex;
    flex-direction: column;
    align-items: center;
    gap: 18px;
  }
  .front-lockup .brand-disc { width: 140px; height: 140px; }
  .front-lockup .brand-name { font-size: 84px; }
  .front-stripe {
    position: absolute;
    left: 0; bottom: 0;
    width: 100%;
    height: 16px;
    background: var(--saffron);
  }
</style>
</head>
<body>
<main class="canvas">
  <section class="card card--back" aria-label="Card back with contact details">
    <div class="details-band">
      <p class="holder-name">Marla Penrick</p>
      <span class="divider"></span>
      <p class="contact contact--social"><span class="social-dot"></span>calmcradlestudiolakebay</p>
      <p class="contact contact--phone">
        <svg class="phone-icon" viewBox="0 0 16 26" aria-hidden="true">
          <rect x="1" y="1" width="14" height="24" rx="2.5" fill="none" stroke="currentColor" stroke-width="1.6"/>
          <line x1="6" y1="21" x2="10" y2="21" stroke="currentColor" stroke-width="1.6"/>
        </svg>
        0482 315 746
      </p>
    </div>
    <div class="brand-band">
      <span class="brand-disc"></span>
      <p class="brand-name">Calm Cradle</p>
    </div>
  </section>

  <section class="card card--front" aria-label="Card front with brand name">
    <div class="front-lockup">
      <span class="brand-disc"></span>
      <p class="brand-name">Calm Cradle</p>
    </div>
    <span class="front-stripe"></span>
  </section>
</main>
</body>
</html>
```